Menu Board

Hi Marlene,

I would like you to design for me a menu board for all my products.

The layout I have hand drawn for you so just follow my layout.

Pho
Noodle salads
Rice
StirFry with Thick Rice Noodles
Spring Rolls Ricepaper Rolls

Poster Size: AO Vertical ( 841W x 1189H)

There are more photos of the rice dishes but I thought I can send this through so you can start and I can send you the rest of the photos when I get back from my photographer.

I will have items descriptions to follow also

• Here are the rest of the photos >

```html
<!DOCTYPE html>
<html lang="en">
<head>
<meta charset="utf-8">
<title>Lantern Lane Menu Board</title>
<link href="https://fonts.googleapis.com/css2?family=Bebas+Neue&family=Michroma&display=swap" rel="stylesheet">
<style>
  :root {
    --bg-light: #4d4d4f;
    --bg-dark: #262628;
    --orange: #f08a1c;
    --orange-deep: #c8650c;
    --white: #ffffff;
    --plate: #f3f1ee;
    --broth: #7a4a22;
    --greens: #5e8a3a;
    --noodle: #d9b98a;
    --wood: #c9935a;
  }
  * { margin: 0; padding: 0; box-sizing: border-box; }
  html, body { width: 849px; height: 1200px; overflow: hidden; background: var(--bg-dark); }
  .menu-board {
    position: relative; width: 849px; height: 1200px; overflow: hidden;
    background: radial-gradient(ellipse at 60% 25%, var(--bg-light) 0%, #3a3a3c 45%, var(--bg-dark) 100%);
  }
  .ground-arc { position: absolute; left: 0; top: 0; width: 849px; height: 1200px; }
  .brand-mark {
    position: absolute; left: 670px; top: 50px; width: 128px; height: 128px;
    border: 2px solid var(--white); border-radius: 50%;
    display: flex; align-items: center; justify-content: center; text-align: center;
  }
  .brand-name {
    font-family: "Bebas Neue", sans-serif; font-size: 26px; line-height: 1;
    color: var(--orange); letter-spacing: 1px; width: 90px;
  }
  .section-tag { position: absolute; }
  .section-tag svg { position: absolute; left: 0; top: 0; overflow: visible; }
  .section-tag span {
    position: absolute; left: 0; right: 0; display: block; text-align: center;
    font-family: "Bebas Neue", sans-serif; color: var(--white);
    font-size: 40px; line-height: 0.92; letter-spacing: 0.5px;
  }
  .dish { position: absolute; }
  .dish-photo { position: absolute; }
  .bowl {
    border-radius: 50% 50% 46% 46% / 38% 38% 62% 62%;
    background: radial-gradient(ellipse at 50% 32%, var(--broth) 0%, var(--greens) 38%, var(--plate) 62%, #d9d6d1 100%);
  }
  .salad-bowl {
    border-radius: 50% 50% 46% 46% / 38% 38% 62% 62%;
    background: radial-gradient(ellipse at 50% 30%, #7b4a2a 0%, var(--greens) 30%, #e07a35 48%, var(--plate) 64%, #d9d6d1 100%);
  }
  .plate {
    border-radius: 14px; transform: skewX(-10deg);
    background: radial-gradient(ellipse at 50% 50%, #8a5230 0%, var(--greens) 30%, #c9452f 46%, var(--plate) 62%, #e2dfda 100%);
  }
  .plate.rice-fried { background: radial-gradient(ellipse at 50% 50%, #eadcb8 0%, #d9b070 35%, var(--plate) 62%, #e2dfda 100%); }
  .plate.noodles { background: radial-gradient(ellipse at 50% 50%, #8a5a35 0%, #e38a3d 28%, var(--noodle) 45%, var(--plate) 64%, #e2dfda 100%); }
  .plate.spring { background: radial-gradient(ellipse at 45% 55%, #b5702e 0%, #cf8c46 30%, var(--plate) 60%, #e2dfda 100%); }
  .board-wood {
    border-radius: 10px; transform: skewX(-18deg);
    background: radial-gradient(ellipse at 55% 45%, #f4f5ef 0%, #cfe2b4 30%, var(--wood) 55%, #a9743f 100%);
  }
  .dish-name {
    position: absolute; text-align: center; white-space: nowrap;
    font-family: "Michroma", sans-serif; color: var(--white);
    font-size: 17px; line-height: 17px; letter-spacing: 2px; transform: translateX(-50%);
  }
</style>
</head>
<body>
<main class="menu-board">

  <svg class="ground-arc" viewBox="0 0 849 1200" aria-hidden="true">
    <path d="M0 1200 L0 1140 Q424 990 849 1140 L849 1200 Z" fill="var(--orange)"/>
  </svg>

  <div class="brand-mark"><span class="brand-name">LANTERN LANE</span></div>

  <!-- Pho -->
  <div class="section-tag" style="left:68px;top:78px;width:104px;height:106px;">
    <svg width="104" height="106" viewBox="0 0 104 106" aria-hidden="true">
      <polygon points="14,70 78,58 68,84 78,102 20,98" fill="var(--orange-deep)"/>
      <polygon points="0,0 104,8 100,66 4,78" fill="var(--orange)"/>
    </svg>
    <span style="top:16px;">PHO</span>
  </div>
  <div class="dish-photo bowl" role="img" aria-label="Beef pho bowl photo" style="left:155px;top:160px;width:180px;height:120px;"></div>
  <div class="dish-photo bowl" role="img" aria-label="Chicken pho bowl photo" style="left:344px;top:160px;width:180px;height:120px;"></div>
  <div class="dish-photo bowl" role="img" aria-label="Tofu pho bowl photo" style="left:532px;top:160px;width:180px;height:120px;"></div>
  <div class="dish-name" style="left:245px;top:286px;">BEEF</div>
  <div class="dish-name" style="left:434px;top:286px;">CHICKEN</div>
  <div class="dish-name" style="left:615px;top:286px;">TOFU</div>

  <!-- Noodle salad -->
  <div class="section-tag" style="left:48px;top:270px;width:144px;height:116px;">
    <svg width="144" height="116" viewBox="0 0 144 116" aria-hidden="true">
      <polygon points="26,86 120,76 112,98 124,114 30,110" fill="var(--orange-deep)"/>
      <polygon points="0,14 140,0 144,84 4,96" fill="var(--orange)"/>
    </svg>
    <span style="top:14px;">NOODLE<br>SALAD</span>
  </div>
  <div class="dish-photo salad-bowl" role="img" aria-label="Beef noodle salad photo" style="left:96px;top:362px;width:172px;height:118px;"></div>
  <div class="dish-photo salad-bowl" role="img" aria-label="Chicken noodle salad photo" style="left:260px;top:366px;width:166px;height:114px;"></div>
  <div class="dish-photo salad-bowl" role="img" aria-label="BBQ pork noodle salad photo" style="left:416px;top:364px;width:168px;height:116px;"></div>
  <div class="dish-photo salad-bowl" role="img" aria-label="Tofu noodle salad photo" style="left:582px;top:366px;width:174px;height:114px;"></div>
  <div class="dish-name" style="left:188px;top:490px;">BEEF</div>
  <div class="dish-name" style="left:348px;top:490px;">CHICKEN</div>
  <div class="dish-name" style="left:506px;top:490px;">BBQ<br>PORK</div>
  <div class="dish-name" style="left:670px;top:490px;">TOFU</div>

  <!-- Rice -->
  <div class="section-tag" style="left:66px;top:514px;width:100px;height:80px;">
    <svg width="100" height="80" viewBox="0 0 100 80" aria-hidden="true">
      <polygon points="12,50 76,44 68,62 78,78 18,72" fill="var(--orange-deep)"/>
      <polygon points="0,4 98,0 100,50 2,56" fill="var(--orange)"/>
    </svg>
    <span style="top:10px;">RICE</span>
  </div>
  <div class="dish-photo plate" role="img" aria-label="BBQ beef with rice photo" style="left:88px;top:562px;width:172px;height:104px;"></div>
  <div class="dish-photo plate" role="img" aria-label="Lemongrass chilli chicken with rice photo" style="left:260px;top:562px;width:172px;height:104px;"></div>
  <div class="dish-photo plate" role="img" aria-label="Tofu with rice photo" style="left:432px;top:562px;width:172px;height:104px;"></div>
  <div class="dish-photo plate rice-fried" role="img" aria-label="Fried rice photo" style="left:604px;top:562px;width:172px;height:104px;"></div>
  <div class="dish-name" style="left:174px;top:680px;">BBQ<br>BEEF</div>
  <div class="dish-name" style="left:347px;top:680px;">LEMONGRASS<br>CHILLI<br>CHICKEN</div>
  <div class="dish-name" style="left:515px;top:680px;">TOFU</div>
  <div class="dish-name" style="left:695px;top:680px;">FRIED<br>RICE</div>

  <!-- Stir fry rice noodles -->
  <div class="section-tag" style="left:54px;top:742px;width:154px;height:160px;">
    <svg width="154" height="160" viewBox="0 0 154 160" aria-hidden="true">
      <polygon points="36,128 130,122 124,142 136,158 40,154" fill="var(--orange-deep)"/>
      <polygon points="0,8 152,0 154,138 2,132" fill="var(--orange)"/>
    </svg>
    <span style="top:16px;">STIR FRY<br>RICE<br>NOODLES</span>
  </div>
  <div class="dish-photo plate noodles" role="img" aria-label="Beef stir fry rice noodles photo" style="left:230px;top:762px;width:180px;height:104px;"></div>
  <div class="dish-photo plate noodles" role="img" aria-label="Chicken stir fry rice noodles photo" style="left:408px;top:762px;width:180px;height:104px;"></div>
  <div class="dish-photo plate noodles" role="img" aria-label="Tofu stir fry rice noodles photo" style="left:596px;top:762px;width:180px;height:104px;"></div>
  <div class="dish-name" style="left:325px;top:882px;">BEEF</div>
  <div class="dish-name" style="left:503px;top:882px;">CHICKEN</div>
  <div class="dish-name" style="left:686px;top:882px;">TOFU</div>

  <!-- Rolls -->
  <div class="section-tag" style="left:60px;top:950px;width:146px;height:112px;">
    <svg width="146" height="112" viewBox="0 0 146 112" aria-hidden="true">
      <polygon points="28,66 124,62 116,84 128,110 34,104" fill="var(--orange-deep)"/>
      <polygon points="0,6 144,0 146,68 4,72" fill="var(--orange)"/>
    </svg>
    <span style="top:16px;">ROLLS</span>
  </div>
  <div class="dish-photo plate spring" role="img" aria-label="Spring rolls with chilli dipping sauce photo" style="left:236px;top:958px;width:168px;height:104px;"></div>
  <div class="dish-photo board-wood" role="img" aria-label="Rice paper rolls on a wooden board photo" style="left:462px;top:924px;width:200px;height:140px;"></div>
  <div class="dish-name" style="left:325px;top:1084px;">SPRING<br>ROLLS</div>
  <div class="dish-name" style="left:551px;top:1084px;">RICE PAPER<br>ROLLS</div>

</main>
</body>
</html>
```